Quorvin Rapid Pregancy Test Box and Sterile Pouch.

We are a company that manufactures rapid diagnostic tests for pregnancy, drugs of abuse, disease, etc. We would like a box and pouch design for our tests. Each box approx (10 1/4" x 4 3/4"x 2 1/2") should be able to hold 40 pouches and the pouches are 4 6/16" x 2 7/16". We have a design currently, but we are not happy with it. we would prefer a more simple and elegant design. We will be marketing this to mainly hospitals, clinics and distributors and not at-home consumers. The design should have our Quorvin Logo and something that says FDA approved and 99% accuracy.
Updates

Logo, current box design and  current pouch image has been uploaded. Current box design image is for fertility hormones, but project is still for RAPID PREGNANCY TEST.

Target Market(s)

Hospitals, Government agencies, doctors, clinics.

Industry/Entity Type

Marketing

Requirements
Must have
• Box: Size, Logo, FDA approval, must denote femininity.

Pouch design must fit in with box design.

design should be on the horizontal for stacking purposes at hospitals. (read long flat box and pouch)
Nice to have
• Colors to match the color scheme of our Quorvin logo.
Should not have
• exceed size dimensions as our production line is set up for these sizes.

```html
<!DOCTYPE html>
<html lang="en">
<head>
<meta charset="utf-8">
<title>Quorvin Rapid Pregnancy Test Box</title>
<link rel="stylesheet" href="https://fonts.googleapis.com/css2?family=Roboto+Condensed:wght@400;700&display=swap">
<style>
  :root {
    --brand-blue: #0a5caa;
    --lavender: #c9cdec;
    --panel-white: #ffffff;
    --backdrop: #000000;
    --ink-grey: #5a6f95;
  }
  html, body {
    margin: 0;
    width: 1200px;
    height: 1125px;
    overflow: hidden;
    background: var(--backdrop);
    font-family: "Roboto Condensed", Arial, sans-serif;
  }
  .canvas {
    position: relative;
    width: 1200px;
    height: 1125px;
  }
  .box-lid, .box-front {
    position: absolute;
    left: 100px;
    width: 1000px;
    background: var(--panel-white);
    overflow: hidden;
  }
  .box-lid { top: 150px; height: 560px; }
  .box-front { top: 740px; height: 210px; }
  .panel-art {
    position: absolute;
    inset: 0;
    width: 100%;
    height: 100%;
  }
  .wave-blue { fill: var(--brand-blue); }
  .wave-lavender { fill: var(--lavender); }

  .accuracy-claim {
    position: absolute;
    left: 380px;
    top: 58px;
    margin: 0;
    color: var(--brand-blue);
    font-weight: 700;
    font-size: 30px;
    letter-spacing: -0.5px;
  }
  .brand-lockup {
    position: absolute;
    display: flex;
    align-items: center;
    gap: 22px;
    color: var(--brand-blue);
    font-weight: 700;
  }
  .brand-dot {
    border-radius: 50%;
    background: var(--brand-blue);
    flex: none;
  }
  .box-lid .brand-lockup { left: 360px; top: 125px; font-size: 150px; line-height: 1; }
  .box-lid .brand-dot { width: 60px; height: 60px; }
  .product-line {
    position: absolute;
    margin: 0;
    color: var(--brand-blue);
    font-weight: 700;
  }
  .box-lid .product-line { left: 560px; top: 290px; font-size: 28px; }
  .rule {
    position: absolute;
    left: 330px;
    top: 345px;
    width: 570px;
    height: 3px;
    background: var(--brand-blue);
  }
  .pack-count {
    position: absolute;
    left: 340px;
    top: 362px;
    margin: 0;
    color: var(--ink-grey);
    font-size: 18px;
    letter-spacing: 0.5px;
  }
  .cert-badges {
    position: absolute;
    left: 740px;
    top: 385px;
    display: flex;
    gap: 24px;
  }
  .cert-badge {
    width: 60px;
    height: 40px;
    border: 3px solid #111;
    border-radius: 6px;
    box-sizing: border-box;
  }
  .box-front .brand-lockup { left: 330px; top: 55px; font-size: 78px; line-height: 1; gap: 14px; }
  .box-front .brand-dot { width: 34px; height: 34px; }
  .box-front .product-line { left: 420px; top: 140px; font-size: 20px; }
</style>
</head>
<body>
<main class="canvas">
  <section class="box-lid" aria-label="Box lid">
    <svg class="panel-art" viewBox="0 0 1000 560" preserveAspectRatio="none" aria-hidden="true">
      <path class="wave-lavender" d="M150 0 H240 C310 70 335 200 365 330 C395 450 455 520 505 560 H460 C410 520 355 460 325 330 C295 200 250 60 150 0Z"/>
      <path class="wave-blue" d="M0 0 H170 C255 60 295 200 325 330 C355 460 410 520 460 560 H0Z"/>
      <path class="wave-lavender" d="M1000 300 C930 340 880 460 855 560 H885 C905 470 945 370 1000 340Z"/>
      <path class="wave-blue" d="M1000 340 C945 370 905 470 885 560 H1000Z"/>
    </svg>
    <p class="accuracy-claim">✱ 99% Accurate</p>
    <div class="brand-lockup"><span class="brand-dot"></span><span class="brand-name">Quorvin</span></div>
    <p class="product-line">Rapid Diagnostic Pregnancy Tests</p>
    <div class="rule"></div>
    <p class="pack-count">40 POUCHES</p>
    <div class="cert-badges">
      <span class="cert-badge" aria-label="Conformity mark"></span>
      <span class="cert-badge" aria-label="Regulatory approval mark"></span>
    </div>
  </section>

  <section class="box-front" aria-label="Box front panel">
    <svg class="panel-art" viewBox="0 0 1000 210" preserveAspectRatio="none" aria-hidden="true">
      <path class="wave-lavender" d="M220 0 H270 C225 50 205 130 200 210 H170 C175 130 190 50 220 0Z"/>
      <path class="wave-blue" d="M0 0 H220 C190 50 175 130 170 210 H0Z"/>
      <path class="wave-lavender" d="M1000 0 H900 C880 70 850 160 800 210 H830 C880 160 905 80 925 0Z"/>
      <path class="wave-blue" d="M1000 0 H925 C905 80 880 160 830 210 H1000Z"/>
    </svg>
    <div class="brand-lockup"><span class="brand-dot"></span><span class="brand-name">Quorvin</span></div>
    <p class="product-line">Rapid Diagnostic Pregnancy Tests</p>
  </section>
</main>
</body>
</html>
```